Medical Device - Case Study Template

We need a TEMPLATE that we can reuse to write various case studies about the medical equipment solutions we provide. It will be a double sided letter sized with a modern design that conveys a feeling of expertise, innovation and highly personable service AND be consistent with the brand guide. The content will be divided into a few sections:

- Situation (200-250 words)
- Challenge (100-120 words)
- Solution (100-120 words)
- Results (100-120 words)
- Conclusion (100-120 words)

Additionally, there will need to be a call to action, inviting people to send an email for more information and a short "About Talvo" section (approx. 40 words).

For device picture placeholders, feel free to use any random small benchtop medical device.

```html
<!DOCTYPE html>
<html lang="en">
<head>
<meta charset="utf-8">
<title>Talvo Medical Device Case Study</title>
<link href="https://fonts.googleapis.com/css2?family=Oswald:wght@600;700&family=Lato:ital,wght@0,300;0,400;0,700;1,700&display=swap" rel="stylesheet">
<style>
:root{
  --bg:#e6e7e9;
  --orange:#f0843a;
  --navy:#0f2857;
  --blue:#0d5aa7;
  --steel:#8aa9c8;
  --quote:#6c8db5;
  --ink:#3a3f47;
  --white:#ffffff;
}
*{margin:0;padding:0;box-sizing:border-box}
html,body{width:1200px;height:887px;overflow:hidden;background:var(--bg)}
body{position:relative;font-family:"Lato",sans-serif;color:var(--ink)}
.page{position:absolute;width:498px;height:704px;background:var(--white);overflow:hidden;box-shadow:4px 5px 10px rgba(0,0,0,.22)}
.page--front{left:88px;top:88px}
.page--back{left:616px;top:89px}
.abs{position:absolute}
.band{position:absolute;left:0;top:0;width:100%;height:210px;background:var(--orange)}
.band__tab{position:absolute;left:0;top:0;width:208px;height:9px;background:var(--navy)}
.heading{font-family:"Oswald",sans-serif;font-weight:700;text-transform:uppercase;letter-spacing:.2px;line-height:1;color:var(--blue);font-size:23px}
.heading--white{color:var(--white)}
.heading--orange{color:var(--orange)}
.body{font-size:8.6px;line-height:10px;font-weight:300;text-align:justify}
.body p+p{margin-top:10px}
.body--white{color:var(--white)}
.quote{font-family:"Oswald",sans-serif;font-weight:600;font-size:10px;line-height:12px;color:var(--quote)}
.brand{display:flex;align-items:center;gap:7px;color:var(--white)}
.brand__dot{width:26px;height:26px;border-radius:50%;background:var(--white)}
.brand__name{font-family:"Lato",sans-serif;font-weight:400;font-size:24px;line-height:1}
.brand__tag{font-size:8px;letter-spacing:.6px}
.title{left:38px;top:124px;font-size:33px;line-height:31px;color:var(--white)}
.title-dash{left:38px;top:114px;width:18px;height:2px;background:var(--blue)}
.icons{left:300px;top:22px;width:190px;height:160px;border-radius:8px;background:radial-gradient(circle at 50% 50%,rgba(255,255,255,.35),rgba(255,255,255,0) 70%)}
.device{left:296px;top:240px;width:156px;height:110px;border-radius:8px;background:linear-gradient(160deg,#f4f5f6,#d6d9dc)}
.callout{left:38px;top:456px;width:222px;height:107px;background:var(--orange);padding:13px 14px;color:var(--white);font-size:9.2px;line-height:11px;font-weight:300;text-align:justify}
.callout__bar{left:38px;top:559px;width:155px;height:4px;background:var(--blue)}
.footer-url{font-size:8.4px;letter-spacing:.5px;color:var(--orange)}
.stat{width:60px;text-align:center}
.stat__hex{display:block;margin:0 auto}
.stat__label{margin-top:4px;font-size:8.6px;line-height:10px;font-weight:300}
.cta{left:252px;top:491px;width:200px;height:71px;padding:9px 16px;color:var(--white)}
.cta__title{font-size:17px;color:var(--white)}
.cta__line{display:flex;align-items:center;gap:8px;margin-top:4px;font-size:11.5px;font-weight:300}
.contact{color:var(--white);font-size:8.6px;line-height:10px;font-weight:300}
</style>
</head>
<body>

<section class="page page--front">
  <div class="band"></div>
  <div class="band__tab"></div>

  <div class="abs brand" style="left:38px;top:42px">
    <span class="brand__dot"></span>
    <div>
      <div class="brand__name">talvo</div>
      <div class="brand__tag">Medical Technology</div>
    </div>
  </div>

  <div class="abs icons" role="img" aria-label="Medical icons arranged in white hexagons"></div>

  <div class="abs title-dash"></div>
  <h1 class="abs heading title">Medical Device<br>Case Study</h1>

  <h2 class="abs heading" style="left:38px;top:245px">Situation</h2>
  <div class="abs body" style="left:38px;top:275px;width:222px">
    <p>Lorem ipsum dolor sit amet, consectetuer adipiscing elit, sed diam nonummy nibh euismod tincidunt ut laoreet dolore magna aliquam erat volutpat. Ut wisi enim ad minim veniam, quis nostrud exerci tation ullamcorper suscipit lobortis nisl ut aliquip ex ea commodo consequat.</p>
    <p>Duis autem vel Lorem ipsum dolor sit amet, consectetuer adipiscing elit, sed diam nonummy nibh euismod tincidunt ut laoreet dolore magna aliquam erat volutpat. Ut wisi enim ad minim veniam, quis nostrud exerci tation ullamcorper suscipit lobortis nisl ut aliquip ex ea commodo consequat.</p>
    <p>Duis autem vel eum iriure dolor in hendrerit in vulputate velit esse molestie consequat, vel illum dolore eu feugiat nulla facilisis at vero eros et accumsan et iusto odio dignissim qui blandit praesent luptatum zzril delenit augue duis dolore te feugait nulla facilisi.</p>
  </div>

  <div class="abs callout">Lorem ipsum dolor sit amet, cons ectetuer adipiscing elit, sed diam nonummy nibh euismod tincidunt ut laoreet dolore magna aliquam erat volutpat. Ut wisi enim ad minim veniam, quis nostrud exerci tation ullamcorper suscipit lobortis nisl ut aliquip ex ea commodo consequat.</div>
  <div class="abs callout__bar"></div>

  <div class="abs body" style="left:38px;top:575px;width:222px">
    <p>Lorem ipsum dolor sit amet, consectetuer adipiscing elit, Lorem ipsum dolor sit amet, consectetuer adipiscing elit, sed diam nonummy nibh euismod tincidunt ut laoreet dolore magna aliquam erat volutpat. Ut wisi enim ad minim veniam, quis nostrud exerci tation ullamcorper suscipit lobortis nisl ut aliquip ex ea commodo consequat.</p>
  </div>

  <div class="abs device" role="img" aria-label="Benchtop fetal monitor with colour display"></div>

  <h2 class="abs heading" style="left:294px;top:378px">Challenge</h2>
  <div class="abs body" style="left:294px;top:410px;width:176px">
    <p>Lorem ipsum dolor sit amet, consectetuer adipiscing elit, sed diam nonummy nibh euismod tincidunt ut laoreet dolore magna aliquam erat volutpat. Ut wisi enim ad minim veniam, quis nostrud exerci tation ullamcorper suscipit lobortis nisl ut aliquip ex ea commodo consequat. Duis autem vel Lorem ipsum dolor sit amet, consectetuer adipiscing elit, sed diam nonummy nibh euismod tincidunt ut laoreet dolore magna aliquam erat volutpat. Ut wisi enim ad minim veniam, quis nostrud exerci tation ullamcorper suscipit lobortis nisl ut aliquip ex ea commodo consequat. Duis autem vel eum iriure dolor in hendrerit in vulputate velit esse molestie consequat, vel illum dolore eu feugiat nulla facilisis at vero</p>
  </div>
  <p class="abs quote" style="left:294px;top:590px;width:180px">Lorem ipsum dolor sit amet, consectetuer adipiscing elit, sed diam nonummy nibh.</p>

  <svg class="abs" style="left:0;top:610px" width="498" height="94" viewBox="0 0 498 94" aria-hidden="true">
    <polygon points="0,56 472,56 498,10 498,94 0,94" fill="var(--steel)"/>
    <polygon points="0,59 474,59 498,17 498,94 0,94" fill="var(--navy)"/>
  </svg>
  <p class="abs footer-url" style="left:39px;top:679px">www.talvomedicaltech.com</p>
</section>

<section class="page page--back">
  <div class="band"></div>
  <div class="band__tab"></div>

  <h2 class="abs heading heading--white" style="left:38px;top:50px">Solution</h2>
  <div class="abs body body--white" style="left:38px;top:84px;width:176px">
    <p>Lorem ipsum dolor sit amet, consectetuer adipiscing elit, sed diam nonummy nibh euismod tincidunt ut laoreet dolore magna aliquam erat volutpat. Ut wisi enim ad minim veniam, quis nostrud exerci tation ullamcorper suscipit lobortis nisl ut aliquip ex ea commodo consequat. Duis autem vel Lorem ipsum dolor sit amet, consectetuer adipiscing elit, sed diam nonummy nibh euismod tincidunt ut laoreet dolore magna aliquam erat volutpat.</p>
  </div>
  <div class="abs body body--white" style="left:254px;top:84px;width:191px">
    <p>Ut wisi enim ad minim veniam, quis nostrud exerci tation ullamcorper suscipit lobortis nisl ut aliquip ex ea commodo consequat. Duis autem vel eum iriure dolor in hendrerit in vulputate velit esse molestie consequat, vel illum dolore eu feugiat nulla facilisis at vero</p>
  </div>

  <h2 class="abs heading" style="left:38px;top:238px">Result</h2>
  <div class="abs body" style="left:38px;top:272px;width:176px">
    <p>Lorem ipsum dolor sit amet, consectetuer adipiscing elit, sed diam nonummy nibh euismod tincidunt ut laoreet dolore magna aliquam erat volutpat. Ut wisi enim ad minim veniam, quis nostrud exerci tation ullamcorper suscipit lobortis nisl ut aliquip ex ea commodo consequat. Duis autem vel Lorem ipsum dolor sit amet, consectetuer adipiscing elit, sed diam nonummy nibh euismod tincidunt ut laoreet dolore magna aliquam erat volutpat. Ut wisi enim ad minim veniam, quis nostrud exerci tation ullamcorper suscipit lobortis nisl ut aliquip ex ea commodo consequat. Duis autem vel eum iriure dolor in hendrerit in vulputate velit esse molestie consequat, vel illum dolore eu feugiat nulla facilisis at vero</p>
  </div>

  <div class="abs stat" style="left:33px;top:447px">
    <svg class="stat__hex" width="42" height="38" viewBox="0 0 42 38"><polygon points="10,0 32,0 42,19 32,38 10,38 0,19" fill="var(--orange)"/><text x="21" y="25" text-anchor="middle" font-family="Oswald, sans-serif" font-weight="700" font-size="15" fill="#fff">30<tspan font-size="8" dy="-6">%</tspan></text></svg>
    <div class="stat__label">Lorem ipsum dolor sit amet</div>
  </div>
  <div class="abs stat" style="left:95px;top:447px">
    <svg class="stat__hex" width="42" height="38" viewBox="0 0 42 38"><polygon points="10,0 32,0 42,19 32,38 10,38 0,19" fill="var(--orange)"/><text x="21" y="25" text-anchor="middle" font-family="Oswald, sans-serif" font-weight="700" font-size="15" fill="#fff">110</text></svg>
    <div class="stat__label">Lorem ipsum dolor sit amet</div>
  </div>
  <div class="abs stat" style="left:159px;top:447px">
    <svg class="stat__hex" width="42" height="38" viewBox="0 0 42 38"><polygon points="10,0 32,0 42,19 32,38 10,38 0,19" fill="var(--orange)"/><text x="21" y="25" text-anchor="middle" font-family="Oswald, sans-serif" font-weight="700" font-size="15" fill="#fff">2B</text></svg>
    <div class="stat__label">Lorem ipsum dolor sit amet</div>
  </div>

  <h2 class="abs heading" style="left:254px;top:238px">Conclusion</h2>
  <div class="abs body" style="left:254px;top:272px;width:191px">
    <p>Lorem ipsum dolor sit amet, consectetuer adipiscing elit, sed diam nonummy nibh euismod tincidunt ut laoreet dolore magna aliquam erat volutpat. Ut wisi enim ad minim veniam, quis nostrud exerci tation ullamcorper suscipit lobortis nisl ut aliquip ex ea commodo consequat. Duis autem vel Lorem ipsum dolor sit amet, consectetuer adipiscing elit, sed diam nonummy nibh euismod tincidunt ut laoreet dolore magna aliquam erat volutpat. Ut wisi enim ad minim veniam, quis nostrud exerci tation ullamcorper suscipit lobortis nisl ut aliquip ex ea commodo consequat. Duis autem vel eum iriure dolor in hendrerit in vulputate velit esse molestie consequat, vel illum dolore eu feugiat nulla facilisis at vero</p>
  </div>
  <p class="abs quote" style="left:254px;top:441px;width:190px">Lorem ipsum dolor sit amet, consectetuer adipiscing elit, sed diam nonummy nibh.</p>

  <svg class="abs" style="left:0;top:500px" width="498" height="204" viewBox="0 0 498 204" aria-hidden="true">
    <polygon points="0,39 474,39 498,-4 498,204 0,204" fill="var(--steel)"/>
    <polygon points="0,42 476,42 498,3 498,204 0,204" fill="var(--navy)"/>
  </svg>

  <svg class="abs" style="left:252px;top:491px" width="200" height="71" viewBox="0 0 200 71" aria-hidden="true">
    <polygon points="0,0 180,0 200,20 200,71 0,71" fill="var(--orange)"/>
  </svg>
  <div class="abs cta">
    <div class="heading cta__title">Call or Email Us</div>
    <div class="cta__line">
      <svg width="11" height="11" viewBox="0 0 24 24" aria-hidden="true"><path d="M6.6 10.8a15 15 0 0 0 6.6 6.6l2.2-2.2c.3-.3.7-.4 1-.2 1.1.4 2.3.6 3.6.6.6 0 1 .4 1 1V20c0 .6-.4 1-1 1A17 17 0 0 1 3 4c0-.6.4-1 1-1h3.5c.6 0 1 .4 1 1 0 1.3.2 2.5.6 3.6.1.3 0 .7-.2 1z" fill="#fff"/></svg>
      <span>555-014-2290</span>
    </div>
    <div class="cta__line" style="margin-top:1px">
      <svg width="11" height="9" viewBox="0 0 24 18" aria-hidden="true"><rect x="1" y="1" width="22" height="16" fill="none" stroke="#fff" stroke-width="2"/><path d="M1 1l11 9 11-9" fill="none" stroke="#fff" stroke-width="2"/></svg>
      <span>info@talvomedicaltech.com</span>
    </div>
  </div>

  <h2 class="abs heading heading--orange" style="left:38px;top:570px">About</h2>
  <div class="abs body body--white" style="left:38px;top:603px;width:172px">
    <p>Lorem ipsum dolor sit amet, consectetuer adipiscing elit, sed diam nonummy nibh euismod tincidunt ut laoreet dolore magna aliquam erat volutpat. Ut wisi enim ad minim veniam, quis nostrud exerci tation ullamcorper suscipit lobortis nisl ut aliquip ex ea commodo consequat.</p>
  </div>

  <div class="abs brand" style="left:260px;top:601px">
    <span class="brand__dot" style="background:var(--orange)"></span>
    <div>
      <div class="brand__name">talvo</div>
      <div class="brand__tag">Medical Technology</div>
    </div>
  </div>
  <p class="abs contact" style="left:260px;top:645px">Address, PO-Box 418 Harbor Road,<br>suite 12, Northvale</p>
  <p class="abs footer-url" style="left:260px;top:677px">www.talvomedicaltech.com</p>
</section>

</body>
</html>
```